Quiet Harbor Pages Blog Re-Do Launch

I need a blog makeover. Someone started for me and they sold their company. The blog is primarily spiritual/inspirational. I would eventually like to monetize and launch some ebooks and/or other products. I am open to suggestions. I am learning as we go along, so please keep that in mind. The final design should be warm and welcoming. I am open to suggestions. I am looking to build a relationship.

Target Market(s)

women, moms, females with chronic health issues, moms of special needs kids, those who need encouragement

Industry/Entity Type

Religious

Number of Pages Required

4 page

Font styles to use
Sans Serif

Colors
eddcec
fdf9cf
ffffff

Requirements
Must have
• I would like my main page to have a short about section, relevant posts, recent posts, and archive posts. The main page should also have a place to subscribe as well a search feature.
Nice to have
• Buttons (grab my button), blogs I follow, e-cart capabilities

```html
<!DOCTYPE html>
<html lang="en">
<head>
<meta charset="utf-8">
<title>Quiet Harbor Pages</title>
<link href="https://fonts.googleapis.com/css2?family=Roboto:ital,wght@0,300;0,400;0,500;0,700;1,400&display=swap" rel="stylesheet">
<style>
:root{
  --pink:#eddcec;
  --pink-line:#dcc0dc;
  --cream:#fdf9cf;
  --gold-a:#f8f2c8;
  --gold-b:#ece29f;
  --gold-line:#ddd08a;
  --white:#ffffff;
  --ink:#2f2f2f;
  --muted:#5a5a5a;
  --accent:#b07bb5;
  --rule:#c9c9c9;
}
*{margin:0;padding:0;box-sizing:border-box}
html,body{width:780px;height:1200px;overflow:hidden;background:var(--white)}
body{position:relative;font-family:"Roboto",Arial,sans-serif;color:var(--ink)}
.abs{position:absolute}
.header-band{left:0;top:0;width:780px;height:100px}
.brand{left:49px;top:26px;display:flex;align-items:center;gap:8px}
.brand-dot{width:22px;height:22px;border-radius:50%;background:var(--accent)}
.brand-name{font-weight:700;font-size:15px;letter-spacing:.5px;color:#4a4a4a}
.search{left:581px;top:23px;width:151px;height:24px;border-radius:12px;background:var(--white);box-shadow:0 0 3px rgba(0,0,0,.12);font-size:8px;color:#777;padding:7px 0 0 14px}
.search svg{position:absolute;right:10px;top:6px}
.nav{left:49px;top:103px;display:flex;align-items:center;font-size:9px;color:#444;letter-spacing:.2px}
.nav a{text-decoration:none;color:inherit;margin-right:30px}
.nav .home{background:var(--cream);border:1px solid #e2d78c;border-radius:12px;padding:6px 14px;margin-right:15px;font-weight:500}
.follow{left:531px;top:110px;font-size:9px;color:#555}
.social{left:595px;top:103px;display:flex;gap:1px}
.social span{width:22px;height:22px;border-radius:50%;background:var(--accent);display:block}
.nav-rule{left:49px;top:134px;width:683px;height:1px;background:var(--rule)}
.hero{left:49px;top:140px;width:683px;height:244px;background:linear-gradient(110deg,#e6ddd0 0%,#b58a6d 35%,#8a5c44 55%,#c7b8a6 80%,#eee8df 100%)}
.dots{left:365px;top:352px;display:flex;gap:6px}
.dots span{width:12px;height:12px;border-radius:50%;background:var(--cream)}
.dots span.on{background:var(--pink);border:2px solid #555}
.section-title{left:49px;top:409px;font-size:14px;font-weight:500;letter-spacing:.3px}
.card{width:215px;height:294px;background:var(--pink);border:1px solid var(--pink-line)}
.card h3{position:absolute;left:10px;top:12px;width:200px;font-size:12.5px;font-weight:500;line-height:16px;color:#333}
.meta{position:absolute;left:-7px;top:46px;height:20px;padding:0 9px 0 16px;background:var(--cream);font-size:7.5px;color:#333;display:flex;align-items:center;gap:4px}
.meta::after{content:"";position:absolute;left:0;bottom:-5px;border-top:5px solid #666;border-left:5px solid transparent}
.meta svg{flex:none}
.card .photo{position:absolute;left:11px;top:80px;width:193px;height:103px}
.card p{position:absolute;left:11px;top:196px;width:195px;font-size:9px;line-height:15.2px;color:var(--muted)}
.card .more{position:absolute;left:11px;top:266px;font-size:8.5px;font-style:italic;color:var(--accent)}
.widget{left:516px;width:216px;background:linear-gradient(180deg,var(--gold-a),var(--gold-b));border:1px solid var(--gold-line)}
.widget h4{position:absolute;left:37px;font-size:14px;font-weight:500;letter-spacing:.3px;color:#333}
.widget .ico{position:absolute;left:14px}
.nl-text{left:13px;top:38px;width:190px;font-size:8.5px;line-height:14px;font-style:italic;color:#555}
.nl-input{left:11px;top:72px;width:193px;height:24px;border-radius:12px;background:var(--white);border:1px solid #d9ccd9;font-size:8px;font-style:italic;color:#666;padding:7px 0 0 15px}
.btn{background:var(--pink);border:1px solid #d3bed3;border-radius:12px;font-size:8.5px;font-weight:500;color:#333;text-align:center;letter-spacing:.3px}
.cart-item .thumb{position:absolute;left:14px;width:52px;height:48px}
.cart-item .txt{position:absolute;left:78px;width:125px;font-size:8.5px;line-height:12px;font-style:italic;color:#333}
.rp{position:absolute;left:15px;width:189px;border-bottom:1px solid #d5c98c;height:40px}
.rp b{display:block;font-weight:400;font-size:9px;color:#333;margin-top:0}
.rp i{display:block;font-style:normal;font-size:7.5px;color:var(--accent);margin-top:5px}
.arch{position:absolute;left:11px;width:193px;height:25px;border-bottom:1px solid #d5c98c;font-size:8.5px;color:#333;padding:7px 0 0 12px}
.arch::before{content:"›";position:absolute;left:10px;top:5px;font-size:10px;color:#555}
.arch span{margin-left:20px}
.pager{left:136px;top:1065px;display:flex;align-items:center;font-size:9px;color:#333}
.pager .older{color:var(--accent);text-decoration:underline;letter-spacing:.2px}
.pager .cur{width:22px;height:21px;background:var(--cream);border:1px solid #e0d48b;text-align:center;line-height:20px;font-size:11px}
.footer{left:0;top:1100px;width:780px;height:100px}
.copy{left:0;top:1162px;width:780px;text-align:center;font-size:8.5px;color:#444}
</style>
</head>
<body>

<svg class="abs header-band" width="780" height="100" viewBox="0 0 780 100" aria-hidden="true">
  <path d="M0 0H780V78C700 58 560 58 420 68 260 80 120 90 0 80Z" fill="var(--pink)"/>
  <path d="M420 68C560 58 700 58 780 78V82C700 64 560 63 420 71Z" fill="var(--cream)"/>
</svg>

<div class="abs brand"><span class="brand-dot"></span><span class="brand-name">QUIET HARBOR PAGES</span></div>

<div class="abs search">Search..
  <svg width="11" height="11" viewBox="0 0 11 11"><circle cx="4.5" cy="4.5" r="3.5" fill="none" stroke="#333" stroke-width="1.5"/><path d="M7 7l3 3" stroke="#333" stroke-width="1.6"/></svg>
</div>

<nav class="abs nav">
  <a class="home">HOME</a><a>ABOUT US</a><a>BLOG</a><a>GALLERY</a><a>CONTACT US</a><a>SHOP</a>
</nav>
<div class="abs follow">FOLLOW US:</div>
<div class="abs social"><span></span><span></span><span></span><span></span><span></span><span></span></div>
<div class="abs nav-rule"></div>

<div class="abs hero" role="img" aria-label="Hands folded in prayer holding a wooden rosary cross over an open book"></div>
<div class="abs dots"><span class="on"></span><span></span><span></span></div>

<h2 class="abs section-title">RECENT POSTS</h2>

<!-- post cards -->
<article class="abs card" style="left:49px;top:440px">
  <h3>Duis aliquam nibh a dui iaculis viverra id a velit....</h3>
  <div class="meta"><svg width="8" height="8" viewBox="0 0 8 8"><rect x=".5" y="1.5" width="7" height="6" fill="none" stroke="#444"/><path d="M.5 3.5h7" stroke="#444"/></svg>Posted on 25 ,2015 &nbsp;| &nbsp;<svg width="7" height="8" viewBox="0 0 7 8"><circle cx="3.5" cy="2" r="2" fill="#444"/><path d="M0 8a3.5 3.5 0 0 1 7 0Z" fill="#444"/></svg>By Admin</div>
  <div class="photo" role="img" aria-label="Small group seated in a circle holding hands in prayer" style="background:linear-gradient(135deg,#d9d4cc,#6d7f9a 45%,#4d8d7c 70%,#c8c2bb)"></div>
  <p>Vivamus egestas risus in magna varius commodo. Sed semper viverra egestas. Etiam pretium porttitor lectus, vel ornare neque porta volutpat...</p>
  <span class="more">Continue Reading</span>
</article>

<article class="abs card" style="left:283px;top:440px">
  <h3>Duis aliquam nibh a dui iaculis viverra id a velit....</h3>
  <div class="meta"><svg width="8" height="8" viewBox="0 0 8 8"><rect x=".5" y="1.5" width="7" height="6" fill="none" stroke="#444"/><path d="M.5 3.5h7" stroke="#444"/></svg>Posted on 25 ,2015 &nbsp;| &nbsp;<svg width="7" height="8" viewBox="0 0 7 8"><circle cx="3.5" cy="2" r="2" fill="#444"/><path d="M0 8a3.5 3.5 0 0 1 7 0Z" fill="#444"/></svg>By Admin</div>
  <div class="photo" role="img" aria-label="Woman in red praying at a wooden church pew" style="background:linear-gradient(135deg,#e8c48c,#6b3d22 40%,#b8283a 60%,#4a2a18)"></div>
  <p>Vivamus egestas risus in magna varius commodo. Sed semper viverra egestas. Etiam pretium porttitor lectus, vel ornare neque porta volutpat...</p>
  <span class="more">Continue Reading</span>
</article>

<article class="abs card" style="left:49px;top:747px">
  <h3>Duis aliquam nibh a dui iaculis viverra id a velit....</h3>
  <div class="meta"><svg width="8" height="8" viewBox="0 0 8 8"><rect x=".5" y="1.5" width="7" height="6" fill="none" stroke="#444"/><path d="M.5 3.5h7" stroke="#444"/></svg>Posted on 25 ,2015 &nbsp;| &nbsp;<svg width="7" height="8" viewBox="0 0 7 8"><circle cx="3.5" cy="2" r="2" fill="#444"/><path d="M0 8a3.5 3.5 0 0 1 7 0Z" fill="#444"/></svg>By Admin</div>
  <div class="photo" role="img" aria-label="Woman in a yellow sweater reading an open bible" style="background:linear-gradient(120deg,#5a3a22,#c99a3e 40%,#e3c98f 60%,#2a2622)"></div>
  <p>Vivamus egestas risus in magna varius commodo. Sed semper viverra egestas. Etiam pretium porttitor lectus, vel ornare neque porta volutpat...</p>
  <span class="more">Continue Reading</span>
</article>

<article class="abs card" style="left:283px;top:747px">
  <h3>Duis aliquam nibh a dui iaculis viverra id a velit....</h3>
  <div class="meta"><svg width="8" height="8" viewBox="0 0 8 8"><rect x=".5" y="1.5" width="7" height="6" fill="none" stroke="#444"/><path d="M.5 3.5h7" stroke="#444"/></svg>Posted on 25 ,2015 &nbsp;| &nbsp;<svg width="7" height="8" viewBox="0 0 7 8"><circle cx="3.5" cy="2" r="2" fill="#444"/><path d="M0 8a3.5 3.5 0 0 1 7 0Z" fill="#444"/></svg>By Admin</div>
  <div class="photo" role="img" aria-label="Silhouettes of people raising hands before a glowing cross" style="background:radial-gradient(circle at 50% 35%,#f3e4c4,#b38a5a 45%,#3d2a1c 90%)"></div>
  <p>Vivamus egestas risus in magna varius commodo. Sed semper viverra egestas. Etiam pretium porttitor lectus, vel ornare neque porta volutpat...</p>
  <span class="more">Continue Reading</span>
</article>

<!-- newsletter -->
<section class="abs widget" style="top:440px;height:142px">
  <svg class="ico" style="top:16px" width="14" height="11" viewBox="0 0 14 11"><rect width="14" height="11" rx="1" fill="var(--accent)"/><path d="M1 1l6 5 6-5" fill="none" stroke="var(--gold-a)" stroke-width="1.2"/></svg>
  <h4 style="top:13px">NEWSLETTER SIGN UP</h4>
  <div class="abs nl-text">Sed semper viverra egestas. Etiam pretium porttitor lectus..</div>
  <div class="abs nl-input">Enter Email Address</div>
  <div class="abs btn" style="left:126px;top:103px;width:78px;height:23px;line-height:22px">SUBSCRIBE</div>
</section>

<!-- e-cart -->
<section class="abs widget" style="top:593px;height:169px">
  <svg class="ico" style="top:17px" width="14" height="12" viewBox="0 0 14 12"><path d="M0 1h2.5l2 7h7l2-5.5H4" fill="none" stroke="var(--accent)" stroke-width="1.6"/><circle cx="5.5" cy="10.5" r="1.3" fill="var(--accent)"/><circle cx="10.5" cy="10.5" r="1.3" fill="var(--accent)"/></svg>
  <h4 style="top:13px">E-CART</h4>
  <div class="cart-item">
    <div class="thumb" role="img" aria-label="Book cover with a couple at a wedding" style="top:39px;background:linear-gradient(135deg,#c9d3d8,#4d4d52 50%,#d9c9a8)"></div>
    <div class="txt" style="top:41px">Vivamus egestas risus in magna varius..</div>
    <div class="abs btn" style="left:78px;top:68px;width:52px;height:18px;line-height:17px;font-size:7.5px">SHOP</div>
  </div>
  <div style="position:absolute;left:14px;top:97px;width:190px;height:1px;background:#d5c98c"></div>
  <div class="cart-item">
    <div class="thumb" role="img" aria-label="Video thumbnail of a worship band on stage" style="top:107px;background:linear-gradient(135deg,#7a2b12,#e08a2c 50%,#3a1a10)"></div>
    <div class="txt" style="top:109px">Vivamus egestas risus in magna varius..</div>
    <div class="abs btn" style="left:78px;top:136px;width:52px;height:18px;line-height:17px;font-size:7.5px">SHOP</div>
  </div>
</section>

<!-- recent posts -->
<section class="abs widget" style="top:773px;height:169px">
  <svg class="ico" style="top:16px" width="12" height="12" viewBox="0 0 12 12"><circle cx="1.6" cy="10.4" r="1.6" fill="var(--accent)"/><path d="M0 5a7 7 0 0 1 7 7M0 1a11 11 0 0 1 11 11" fill="none" stroke="var(--accent)" stroke-width="1.6"/></svg>
  <h4 style="top:13px">RECENT &nbsp;POSTS</h4>
  <div class="rp" style="top:42px"><b>Vivamus egestas risus in magna varius..</b><i>&#9638; Posted on 25 ,2015 &nbsp;| &nbsp;&#9679; By Admin</i></div>
  <div class="rp" style="top:82px"><b>Vivamus egestas risus ..</b><i>&#9638; Posted on 25 ,2015 &nbsp;| &nbsp;&#9679; By Admin</i></div>
  <div class="rp" style="top:122px;border-bottom:0"><b>Vivamus egestas risus in magna varius..</b><i>&#9638; Posted on 25 ,2015 &nbsp;| &nbsp;&#9679; By Admin</i></div>
</section>

<!-- archive -->
<section class="abs widget" style="top:952px;height:138px">
  <svg class="ico" style="top:15px" width="13" height="13" viewBox="0 0 13 13"><rect x=".7" y="2" width="11.6" height="10.3" fill="none" stroke="var(--accent)" stroke-width="1.3"/><path d="M.7 5h11.6M3.5 0v3M9.5 0v3M4.5 5v7M8.5 5v7M.7 8.5h11.6" stroke="var(--accent)" stroke-width="1"/></svg>
  <h4 style="top:13px">ARCHIVE POSTS</h4>
  <div class="arch" style="top:36px"><span>October 2015</span></div>
  <div class="arch" style="top:61px"><span>September 2015</span></div>
  <div class="arch" style="top:85px"><span>August 2015</span></div>
  <div class="arch" style="top:110px;border-bottom:0"><span>July 2015</span></div>
</section>

<div class="abs pager">
  <span class="older">OLDER POSTS</span>
  <span style="margin:0 12px 0 20px;font-size:11px">‹</span>
  <span class="cur">1</span>
  <span style="margin-left:12px;font-size:11px;letter-spacing:1px">2 / 3 / 4</span>
  <span style="margin:0 22px 0 14px;font-size:11px">›</span>
  <span>NEW POSTS</span>
</div>

<svg class="abs footer" width="780" height="100" viewBox="0 0 780 100" aria-hidden="true">
  <path d="M0 20C140 38 300 40 460 28 600 18 700 8 780 12V100H0Z" fill="var(--cream)"/>
  <path d="M0 15C140 33 300 36 460 24 600 14 700 4 780 8V12C700 8 600 18 460 28 300 40 140 38 0 20Z" fill="var(--pink)"/>
</svg>
<div class="abs copy">Copyright © 2015. Quiet Harbor Pages.All Right Reserved</div>

</body>
</html>
```